Dunmore Hale Voss LLC letterhead/envelope/stationary

Design letterhead and envelope based on prior logo design. Design should be conservative and classic for a defense litigation law firm.

Target Market(s)

Businesses, insurance carriers, construction companies, product manufacturers, healthcare providers, employers, municipalities. In short, the target is businesses that may be sued in court and need civil defense attorneys.

Font styles to use
Serif
Sans Serif

Colors
0255a3

Requirements
Must have
• Straightforward design for letterhead and envelopes including digital format for word. Template should be able to be updated for individual attorneys within the firm. Font should be Trajan Pro if possible to match logo (or a similar font). Firm information is Dunmore Hale Voss LLC, 4700 Westfield Terrace, Suite 320, Birmingham, Alabama, 35817. (205)368-2941. other fields that should be included are fax line, direct line, cell phone and email address so that we can update template for each attorney. The color for the logo is 003362
Nice to have
• digital template for microsoft outlook
Should not have
• Busy design/too many graphics

```html
<!DOCTYPE html>
<html lang="en">
<head>
<meta charset="utf-8">
<title>Dunmore Hale Voss LLC Stationery</title>
<link rel="stylesheet" href="https://fonts.googleapis.com/css2?family=Lato:wght@400;700&display=swap">
<style>
  :root {
    --navy: #16345f;
    --navy-text: #1c3560;
    --backdrop: #d7d7d7;
    --paper: #ffffff;
    --ink: #1d1d1d;
    --faint: #e7eaef;
    --shadow: 0 10px 16px rgba(0,0,0,0.28);
  }
  * { box-sizing: border-box; margin: 0; padding: 0; }
  html, body { width: 1200px; height: 1200px; overflow: hidden; }
  body {
    background: var(--backdrop);
    font-family: "Lato", Arial, sans-serif;
    position: relative;
  }
  .sheet, .envelope {
    position: absolute;
    background: var(--paper);
    box-shadow: var(--shadow);
    overflow: hidden;
  }
  .letterhead { left: 58px; top: 268px; width: 513px; height: 664px; }
  .firm-name {
    font-family: "Lato", Arial, sans-serif;
    font-weight: 700;
    color: var(--navy-text);
    line-height: 1.1;
    letter-spacing: 0.04em;
  }
  .letterhead .firm-name { position: absolute; left: 43px; top: 28px; font-size: 15px; width: 160px; }
  .contact-list { position: absolute; left: 286px; top: 26px; list-style: none; }
  .contact-list li {
    display: flex; align-items: center; gap: 5px;
    font-size: 7.4px; color: var(--ink); height: 11.8px; white-space: nowrap;
  }
  .contact-list svg { width: 8px; height: 8px; flex: none; }
  .rule-vertical { position: absolute; width: 1px; background: var(--navy); }
  .letterhead .rule-vertical { left: 381px; top: 24px; height: 47px; }
  .address { color: var(--navy-text); font-size: 7.2px; line-height: 9.6px; position: absolute; }
  .letterhead .address { left: 389px; top: 36px; }
  .letter-body {
    position: absolute; left: 43px; top: 126px; width: 430px;
    font-size: 9.9px; line-height: 17.6px; color: var(--ink);
  }
  .letter-body p { margin-bottom: 17.6px; }
  .signature-area {
    width: 126px; height: 44px; margin: -2px 0 4px;
    background: linear-gradient(90deg, #f1f1f1, #e6e6e6);
  }
  .watermark {
    position: absolute; right: 28px; top: 568px;
    font-size: 26px; font-weight: 700; color: var(--faint); letter-spacing: 0.04em;
    white-space: nowrap;
  }
  .footer-band { position: absolute; left: 0; bottom: 0; width: 100%; height: 22px; background: var(--navy); }

  .envelope { left: 629px; width: 513px; height: 232px; }
  .env-window { top: 94px; }
  .env-stacked { top: 354px; }
  .env-back-white { top: 614px; }
  .env-back-navy { top: 878px; }
  .env-window .firm-name { position: absolute; left: 18px; top: 18px; font-size: 11px; width: 84px; }
  .env-window .rule-vertical { left: 106px; top: 18px; height: 30px; }
  .env-window .address { left: 113px; top: 16px; }
  .env-stacked .firm-name { position: absolute; left: 18px; top: 18px; font-size: 11px; width: 110px; }
  .env-stacked .address { left: 19px; top: 56px; }
  .flap { position: absolute; left: 0; top: 0; width: 513px; height: 76px; }
  .flap-name {
    position: absolute; left: 0; top: 26px; width: 513px; text-align: center;
    font-size: 17px; font-weight: 700; letter-spacing: 0.04em;
  }
  .env-back-white .flap-name { color: var(--navy-text); }
  .env-back-navy .flap-name { color: var(--paper); }
</style>
</head>
<body>

<section class="sheet letterhead">
  <div class="firm-name">Dunmore Hale Voss LLC</div>
  <ul class="contact-list">
    <li><svg viewBox="0 0 8 8"><rect width="8" height="8" rx="1.5" fill="#16345f"/><rect x="2.7" y="1.4" width="2.6" height="5.2" rx="0.5" fill="#fff"/></svg>(205)368-2941</li>
    <li><svg viewBox="0 0 8 8"><rect width="8" height="8" rx="1.5" fill="#16345f"/><path d="M2 2.2c0 2 1.8 3.8 3.8 3.8l.4-1-1-.6-.6.5C3.8 4.5 3.5 4.2 3.1 3.4l.5-.6-.6-1z" fill="#fff"/></svg>(205)368-2941</li>
    <li><svg viewBox="0 0 8 8"><rect width="8" height="8" rx="1.5" fill="#16345f"/><rect x="1.8" y="3.4" width="4.4" height="2.8" fill="#fff"/><rect x="2.6" y="1.6" width="2.8" height="1.6" fill="#fff"/></svg>(205)368-2941</li>
    <li><svg viewBox="0 0 8 8"><rect width="8" height="8" rx="1.5" fill="#16345f"/><rect x="1.6" y="2.4" width="4.8" height="3.2" fill="#fff"/><path d="M1.6 2.4L4 4.3 6.4 2.4" stroke="#16345f" stroke-width="0.5" fill="none"/></svg>info@dhvlaw.com</li>
  </ul>
  <div class="rule-vertical"></div>
  <p class="address">4700 Westfield Terrace,<br>Suite 320, Birmingham,<br>Alabama, 35817</p>

  <div class="letter-body">
    <p>Lorem Ipsum is simply</p>
    <p>&nbsp;dummy text of the printing and typesetting industry. Lorem Ipsum has been the industry's standard dummy text ever since the 1500s, when an unknown printer took a galley of type and scrambled it to make a type specimen book. It has survived not only five centuries, but also the leap into electronic typesetting, remaining essentially unchanged.</p>
    <p>It is a long established fact that a reader will be distracted by the readable content of a page when looking at its layout. The point of using Lorem Ipsum is that it has a more-or-less normal distribution of letters, as opposed to using 'Content here, content here', making it look like readable English. Many desktop publishing packages and web page editors now use Lorem Ipsum as their default model text, and a search for 'lorem ipsum' will uncover many web sites still in their infancy. Various versions have evolved over the years, sometimes by accident, sometimes on purpose (injected humour and the like).</p>
    <p>&nbsp;Contrary to popular belief, Lorem Ipsum is not simply random text. It has roots in a piece of classical Latin literature from 45 BC, making it over 2000 years old. Richard McClintock, a Latin professor at Hampden-Sydney College in Virginia, looked up one of the more obscure Latin words, consectetur, from a Lorem Ipsum passage,</p>
    <p style="margin-bottom:4px">Lorem Ipsum</p>
    <div class="signature-area" role="img" aria-label="Handwritten signature"></div>
    <p>Lorem Ipsum is a dummy</p>
  </div>

  <div class="watermark" aria-hidden="true">Dunmore Hale Voss</div>
  <div class="footer-band"></div>
</section>

<section class="envelope env-window">
  <div class="firm-name">Dunmore Hale Voss LLC</div>
  <div class="rule-vertical"></div>
  <p class="address">4700 Westfield Terrace,<br>Suite 320, Birmingham,<br>Alabama, 35817</p>
</section>

<section class="envelope env-stacked">
  <div class="firm-name">Dunmore Hale Voss LLC</div>
  <p class="address">4700 Westfield Terrace,<br>Suite 320, Birmingham,<br>Alabama, 35817</p>
</section>

<section class="envelope env-back-white">
  <svg class="flap" viewBox="0 0 513 76" aria-hidden="true">
    <defs><filter id="flapShadow" x="-5%" y="-20%" width="110%" height="150%"><feDropShadow dx="0" dy="3" stdDeviation="3" flood-opacity="0.25"/></filter></defs>
    <path d="M0 0H513L488 70Q486 72 480 72L31 74Q25 74 23 70Z" fill="#fff" filter="url(#flapShadow)"/>
  </svg>
  <div class="flap-name">Dunmore Hale Voss</div>
</section>

<section class="envelope env-back-navy">
  <svg class="flap" viewBox="0 0 513 76" aria-hidden="true">
    <path d="M0 0H513L490 70Q488 73 482 73L31 74Q25 74 23 70Z" fill="#16345f"/>
  </svg>
  <div class="flap-name">Dunmore Hale Voss</div>
</section>

</body>
</html>
```